FLYER: Human Factors in Traffic Crashes - Analysis of Drivers' Responses - training

We are hosting a class in Australia 30, November to 4, December 2020. I would like to have a flyer designed to "sell" the class with description of course topics. I have uploaded a flyer I started on my own but I want it to be professional. Dr. Pelloway only gets to AU every 3-5 years to teach from the US. I would like to have some type of roadway scenery, prefer a nighttime scene.

Target Market(s)

Accident reconstructionists and engineers, police reconstructionists.

Font styles to use
Serif

Colors
fec214

Requirements
Must have
• Name of course and course topics, location of course, price, website and contact information.
Nice to have
• Some type of roadway background, possibly a nighttime scene on a roadway.

```html
<!DOCTYPE html>
<html lang="en">
<head>
<meta charset="utf-8">
<title>Human Factors in Traffic Crashes – Open Class Flyer</title>
<link href="https://fonts.googleapis.com/css2?family=Bebas+Neue&family=Montserrat:wght@400;600;700&display=swap" rel="stylesheet">
<style>
:root{
  --yellow:#f6b124;
  --yellow-soft:#fdc75c;
  --dark:#3c3c3c;
  --ink:#2b2b2b;
  --panel:#efefef;
  --cell:#f4f4f4;
  --cell-alt:#e4e4e4;
  --backdrop:#8d8d8d;
  --paper:#ffffff;
}
*{box-sizing:border-box;margin:0;padding:0}
html,body{width:1200px;height:2400px;overflow:hidden;background:var(--backdrop)}
.flyer{position:absolute;left:0;top:422px;width:1200px;height:1556px;background:var(--paper);font-family:"Montserrat",sans-serif;color:var(--dark)}
.brand{position:absolute;left:57px;top:92px;display:flex;align-items:center;gap:18px}
.brand-mark{width:54px;height:54px;background:var(--yellow)}
.brand-name{font-family:"Bebas Neue",sans-serif;font-size:64px;line-height:1;color:var(--ink);letter-spacing:1px}
.title{position:absolute;left:54px;top:300px;width:540px;font-family:"Bebas Neue",sans-serif;line-height:.92}
.title span{display:block}
.t-yellow{color:var(--yellow)}
.t-dark{color:var(--dark)}
.t1{font-size:104px}
.t2{font-size:80px}
.t3{font-size:128px}
.t4{font-size:84px}
.open-class{position:absolute;left:54px;top:664px;width:521px;height:53px;display:flex;font-family:"Bebas Neue",sans-serif;font-size:44px;line-height:53px}
.open-class .label{width:198px;background:var(--yellow);color:var(--dark);padding-left:22px}
.open-class .place{flex:1;background:var(--dark);color:#fff;padding-left:34px}
.presenter{position:absolute;left:54px;top:772px;font-weight:700;font-size:22px;line-height:1.3;color:#444}
.info-row{position:absolute;left:54px;width:537px;display:flex;gap:6px}
.row-location{top:870px;height:113px}
.row-fee{top:995px;height:88px}
.info-key{width:165px;background:var(--yellow-soft);border:2px solid #555;font-weight:700;font-size:22px;padding:0 12px;display:flex;align-items:center;line-height:1.1}
.info-val{flex:1;border:2px solid #555;background:var(--cell);font-size:20px;line-height:1.22;padding:6px 12px}
.info-val b{font-weight:700}
.fee-split{flex:1;border:2px solid #555;display:flex}
.fee-split div{flex:1;display:flex;align-items:center;padding-left:12px;font-weight:700;font-size:21px;background:var(--cell)}
.fee-split div+div{background:var(--cell-alt);padding-left:24px}
.note{position:absolute;left:54px;top:1126px;width:540px;font-size:20px;line-height:1.2}
.register{position:absolute;left:54px;top:1227px;width:536px;height:162px;background:var(--yellow);padding:24px 20px}
.register h3{font-size:25px;font-weight:700;color:var(--ink);margin-bottom:14px}
.register p{font-size:20px;line-height:1.2;color:var(--ink)}
.visit-bar{position:absolute;left:54px;top:1407px;width:1096px;height:90px;background:var(--dark);color:#fff;font-family:"Bebas Neue",sans-serif;font-size:35px;line-height:90px;text-align:center}
.band{position:absolute;left:670px;width:480px;height:27px;background:var(--yellow)}
.band-top{top:0}
.band-mid{top:490px}
.photo{position:absolute;left:670px;top:42px;width:480px;height:430px;background:linear-gradient(180deg,#bfe0f3 0%,#4f8f4a 22%,#2f6b3a 40%,#1f8fb8 60%,#0f6d97 100%)}
.topics{position:absolute;left:670px;top:534px;width:480px;height:855px;background:var(--panel);padding:34px 24px 0}
.topics h2{font-size:25px;font-weight:700;color:var(--ink);letter-spacing:.5px;margin-bottom:20px}
.topics ul{list-style:none}
.topics li{position:relative;padding-left:24px;font-size:18.5px;line-height:1.15;color:#555;margin-bottom:21px}
.topics li::before{content:"";position:absolute;left:0;top:5px;width:10px;height:10px;border:1.5px solid #666;border-radius:50%}
</style>
</head>
<body>
<article class="flyer">
  <header class="brand">
    <div class="brand-mark"></div>
    <div class="brand-name">ROADLINE SAFETY GROUP</div>
  </header>

  <h1 class="title">
    <span class="t1 t-yellow">HUMAN FACTORS</span>
    <span class="t2 t-dark">IN TRAFFIC CRASHES</span>
    <span class="t3 t-yellow">ANALYSIS OF</span>
    <span class="t4 t-dark">DRIVERS’ RESPONSES</span>
  </h1>

  <div class="open-class"><div class="label">OPEN CLASS:</div><div class="place">SEACLIFF NSW</div></div>

  <p class="presenter">PRESENTED BY: Daniel Pelloway Ph.D.<br>World renowned Human Factors expert</p>

  <div class="info-row row-location">
    <div class="info-key">LOCATION</div>
    <div class="info-val"><b>Harbour Point Lodge<br>Cove Ridge Reserve</b><br>12 Lookout Point Road,<br>Seacliff NSW</div>
  </div>
  <div class="info-row row-fee">
    <div class="info-key">COURSE<br>FEE:</div>
    <div class="fee-split"><div>$1,730 AU</div><div>$1,200 USD</div></div>
  </div>

  <p class="note">It has been 3 years since Dr. Pelloway has come to<br>AU to teach, don’t miss out on<br>this year’s class.</p>

  <section class="register">
    <h3>REGISTER ON OUR WEBSITE:</h3>
    <p>www.roadlinesafety.com or<br>Contact: Mara@roadlinesafety.com<br>555-013-2047</p>
  </section>

  <div class="band band-top"></div>
  <div class="photo" role="img" aria-label="Aerial photo of a green harbour cove with a ferry, boats and a wharf"></div>
  <div class="band band-mid"></div>

  <section class="topics">
    <h2>COURSE TOPICS</h2>
    <ul>
      <li>Perception-Response Time<br>Response to slow moving or<br>stopped vehicles on multilane<br>high speed roads</li>
      <li>Nighttime recognition</li>
      <li>Headlight mapping demonstration<br>and instruction</li>
      <li>Driver decision making</li>
      <li>Research in IDRR</li>
      <li>Gap acceptance for left turns, right<br>turns, and through movements for<br>drivers, riders, and pedestrians</li>
      <li>Pedestrian walking speeds</li>
      <li>Acceleration</li>
      <li>Lateral acceleration (swerving) for<br>cars, motorcycles, and commercial<br>vehicles</li>
      <li>Forward and backward acceleration<br>of cars, motorcycles and commercial<br>vehicles</li>
      <li>Drivers’ responses to green and<br>yellow traffic signals, deceleration<br>choice, reaction time and probability<br>of stopping</li>
    </ul>
  </section>

  <div class="visit-bar">VISIT WWW.ROADLINERESEARCH.COM/ABOUT/ &nbsp;TO LEARN MORE ABOUT DR. PELLOWAY</div>
</article>
</body>
</html>
```